Talvera Web site

Talvera is a trade name for Dresgan enterprises llc, would like Dresgan mentioned but not prominent.

Use current logo to base colors and look/feel of website. Modern trendy look.

Talvera Technical Services - "Irrevocably committed to your success"

Website design for a nation wide service based company

Networking, AV, access control, automation, EAS, project management, consulting, electrical, design, service staffing

Hostwick hosts our URL's

Questions-
Who owns the content once accepted.
How is the content delivered to build site
How do we adjust. or add to content once published

Target Market(s)

commercial and retail technical services. IE, we provide technical services for retail and commercial vertical markets

Industry/Entity Type

Trade

Coding

Coded - Design and coding required

Number of Pages Required

5+ page

Font styles to use
Sans Serif

Colors
3276b5

Requirements
Must have
• Pages-
• About/info, contact, services, customers log in portal, social media links
• links to outside web based software portals
• Call through (call me) links

```html
<!DOCTYPE html>
<html lang="en">
<head>
<meta charset="utf-8">
<title>Talvera Technical Services</title>
<link rel="stylesheet" href="https://fonts.googleapis.com/css2?family=Open+Sans:wdth,wght@75..100,300..800&display=swap">
<style>
:root{
  --brand:#3276b5;
  --brand-dark:#1f5fa8;
  --ring:#2f8fe8;
  --green:#6cbb2f;
  --ink:#4a4a4a;
  --muted:#6b6b6b;
  --accent-red:#d2413a;
  --band:#eef0f5;
  --footer:#2a2a2a;
  --footer-bottom:#1d1d1d;
  --line:#d9dce3;
  --white:#ffffff;
}
*{margin:0;padding:0;box-sizing:border-box}
html,body{width:709px;height:1200px;overflow:hidden;background:var(--white)}
body{position:relative;font-family:"Open Sans",Arial,sans-serif;color:var(--ink)}
.abs{position:absolute}

/* header */
.site-header{position:absolute;left:0;top:0;width:709px;height:110px;border-bottom:2px solid var(--brand)}
.brand{left:58px;top:30px;display:flex;align-items:center;gap:8px}
.brand-mark{width:34px;height:34px;border-radius:50%;background:var(--brand)}
.brand-name{font-size:18px;font-weight:800;color:var(--brand);letter-spacing:.5px;line-height:1}
.brand-sub{font-size:7px;font-weight:700;color:var(--brand);letter-spacing:.4px;margin-top:3px}
.call{left:342px;top:40px;display:flex;align-items:center;gap:9px;font-size:10px;color:#333}
.call b{font-size:12px;font-weight:400}
.search{left:519px;top:40px;width:131px;height:18px;border:1px solid #cfcfcf;display:flex}
.search span{flex:1;font-size:7px;font-style:italic;color:#aaa;padding:4px 7px}
.search i{width:23px;background:#8a8a8a;display:flex;align-items:center;justify-content:center}
.main-nav{top:83px;left:231px;height:27px;display:flex;font-size:7.5px;color:#333}
.main-nav a{display:flex;align-items:center;text-decoration:none;color:inherit;padding:0 16px}
.main-nav a.active{background:var(--brand);color:var(--white);padding:0 13px}

/* hero */
.hero{left:0;top:110px;width:709px;height:279px;background:radial-gradient(ellipse at 55% 40%,#7db4d8 0%,#3f7ea8 45%,#16405e 100%)}
.hero h1{position:absolute;left:0;width:100%;text-align:center;color:var(--white);font-stretch:75%;font-weight:700;text-shadow:0 2px 4px rgba(0,0,0,.35)}
.hero .line1{top:88px;font-size:27px}
.hero .line2{top:121px;font-size:33px}
.hero-arrows{left:337px;top:169px;display:flex;gap:3px}

/* welcome */
.welcome-photo{left:58px;top:421px;width:228px;height:116px;border:3px solid var(--white);outline:1px solid #ccc;box-shadow:0 6px 14px rgba(0,0,0,.25);background:linear-gradient(120deg,#c9a27e,#e6ddd2 45%,#9fb0c2)}
.section-title{font-size:14px;font-weight:700;color:#555;letter-spacing:.2px}
.welcome-title{left:322px;top:417px}
.welcome-text{left:322px;top:445px;width:328px;font-size:6px;line-height:11.7px;color:var(--muted);text-align:justify}
.btn{background:var(--brand);color:var(--white);font-size:6.5px;font-weight:700;display:flex;align-items:center;justify-content:center;box-shadow:0 2px 0 var(--brand-dark)}
.read-more{left:322px;top:518px;width:61px;height:19px}

/* services */
.services{left:0;top:570px;width:709px;height:225px;background:var(--band)}
.services-title{left:0;width:709px;top:15px;text-align:center}
.services-arrows{left:628px;top:18px;display:flex;gap:3px}
.service{position:absolute;top:53px;width:155px;text-align:center}
.service svg{display:block;margin:0 auto}
.service h3{font-size:9px;font-weight:600;color:#333;margin-top:12px}
.service p{font-size:6px;line-height:11px;color:#555;margin-top:5px}
.service .more{font-size:6px;color:var(--accent-red);margin-top:5px}
.divider{top:145px;width:1px;height:52px;background:var(--line)}

/* testimonials + login */
.col-title{top:817px;text-align:center}
.card{background:var(--white);box-shadow:0 1px 5px rgba(0,0,0,.22)}
.testimonial{left:58px;top:853px;width:368px;height:141px}
.avatar{left:159px;top:11px;width:50px;height:50px;border-radius:50%;border:3px solid #eee;background:linear-gradient(#8c6a55,#c9a893)}
.author{left:0;width:100%;top:67px;text-align:center;font-size:6.5px;color:var(--accent-red)}
.quote{left:40px;top:91px;width:290px;font-size:6.3px;line-height:11.7px;text-align:center;color:#444}
.qmark{font-size:22px;color:#888;font-family:Georgia,serif;line-height:1}
.login{left:460px;top:853px;width:190px;height:141px}
.field{position:absolute;left:18px;width:154px;border:1px solid #d6d6d6;font-size:6px;color:#aaa;padding:5px 8px}
.login-btn{left:18px;top:108px;width:55px;height:17px;font-weight:400}

/* footer */
.footer{left:0;top:1020px;width:709px;height:148px;background:var(--footer);color:#e6e6e6}
.footer h4{position:absolute;top:18px;font-size:7.5px;font-weight:700;color:var(--white)}
.footer-about{left:58px;top:48px;width:189px;font-size:6px;line-height:11.6px;text-align:justify}
.footer-maker{left:58px;top:104px;font-size:16px;font-weight:700;letter-spacing:1px;color:rgba(50,118,181,.55)}
.footer-menu{left:310px;top:46px;list-style:none;font-size:6px;line-height:11.6px}
.footer-menu li::before{content:"›";margin-right:8px;color:#bbb}
.news{left:440px;display:flex;gap:16px}
.news-thumb{width:30px;height:29px;background:linear-gradient(135deg,#9fc3dc,#e8eef3)}
.news p{font-size:6px;line-height:11.6px;width:170px;margin-top:-4px}
.copy-bar{left:0;top:1168px;width:709px;height:32px;background:var(--footer-bottom)}
.copy{left:58px;top:11px;font-size:5.6px;color:#8a8a8a}
.social{left:551px;top:10px;display:flex;gap:5px}
.social span{width:11px;height:11px;border-radius:50%;background:#5e5e5e}
</style>
</head>
<body>

<header class="site-header">
  <div class="abs brand">
    <span class="brand-mark"></span>
    <div>
      <div class="brand-name">TALVERA</div>
      <div class="brand-sub">TECHNICAL SERVICES</div>
    </div>
  </div>
  <div class="abs call">
    <svg width="22" height="20" viewBox="0 0 22 20"><path d="M4 10a7 7 0 1 0 3-5.7" fill="none" stroke="var(--brand)" stroke-width="2"/><path d="M3 2l4 2.5-3.5 2z" fill="var(--brand)"/><text x="11" y="13" font-size="7" font-weight="700" text-anchor="middle" fill="var(--brand)" font-family="Open Sans,sans-serif">24</text></svg>
    <span>CALL US : <b>(08) 5550 123</b></span>
  </div>
  <div class="abs search">
    <span>Search</span>
    <i><svg width="8" height="8" viewBox="0 0 8 8"><circle cx="3.2" cy="3.2" r="2.3" fill="none" stroke="#fff" stroke-width="1.1"/><path d="M5 5l2.4 2.4" stroke="#fff" stroke-width="1.2"/></svg></i>
  </div>
  <nav class="abs main-nav">
    <a class="active" href="#">HOME</a>
    <a href="#">ABOUT US</a>
    <a href="#">SERVICES</a>
    <a href="#">CUSTOMER LOG-IN</a>
    <a href="#">TESTIMONIALS</a>
    <a href="#" style="padding-right:0">CONTACT</a>
  </nav>
</header>

<section class="abs hero" role="img" aria-label="Networked laptops on desks joined by glowing data links, in blue tones">
  <h1 class="line1">IRREVOCABLY COMMITTED TO YOUR</h1>
  <h1 class="line2">SUCCESS</h1>
  <div class="abs hero-arrows">
    <svg width="15" height="15" viewBox="0 0 15 15"><circle cx="7.5" cy="7.5" r="6.5" fill="none" stroke="#fff" stroke-width="1.3"/><path d="M9.5 7.5H5M7 5.3L4.8 7.5 7 9.7" fill="none" stroke="#fff" stroke-width="1.3"/></svg>
    <svg width="15" height="15" viewBox="0 0 15 15"><circle cx="7.5" cy="7.5" r="6.5" fill="none" stroke="#fff" stroke-width="1.3"/><path d="M5.5 7.5H10M8 5.3l2.2 2.2L8 9.7" fill="none" stroke="#fff" stroke-width="1.3"/></svg>
  </div>
</section>

<section class="welcome">
  <div class="abs welcome-photo" role="img" aria-label="Team of office staff seated at a meeting table"></div>
  <h2 class="abs section-title welcome-title">WELCOME</h2>
  <p class="abs welcome-text">Sed ut perspiciatis unde omnis iste natus error sit voluptatem accusantium doloremque laudantium, totam rem aperiam, eaque ipsa quae ab illo inventore veritatis et quasi architecto Beatae vitae dicta sunt explicabo. Nemo enim ipsam voluptatem quia voluptas sit aspernatur aut odit aut fugit, sed quia consequuntur magni dolores eos qui Ratione voluptatem sequi nesciunt. Neque porro quisquam est, qui dolorem ipsum quia dolor sit amet, consectetur</p>
  <a class="abs btn read-more">READ MORE</a>
</section>

<section class="abs services">
  <h2 class="abs section-title services-title">SERVICES</h2>
  <div class="abs services-arrows">
    <svg width="9" height="9" viewBox="0 0 9 9"><circle cx="4.5" cy="4.5" r="4.5" fill="#b5b8bf"/><path d="M5.3 2.6L3.4 4.5l1.9 1.9" fill="none" stroke="#fff" stroke-width="1"/></svg>
    <svg width="9" height="9" viewBox="0 0 9 9"><circle cx="4.5" cy="4.5" r="4.5" fill="#b5b8bf"/><path d="M3.7 2.6l1.9 1.9-1.9 1.9" fill="none" stroke="#fff" stroke-width="1"/></svg>
  </div>

  <div class="service" style="left:45px">
    <svg width="74" height="74" viewBox="0 0 74 74"><circle cx="37" cy="37" r="33" fill="#fff" stroke="var(--ring)" stroke-width="6"/><path d="M37 4a33 33 0 0 0-26 53" fill="none" stroke="var(--brand-dark)" stroke-width="6"/><g fill="var(--green)"><rect x="28" y="29" width="18" height="4"/><rect x="28" y="35" width="18" height="4"/><rect x="28" y="41" width="18" height="4"/></g></svg>
    <h3>ACCESS CONTROL</h3>
    <p>"But I must explain to you how all this And praising pain was born and I will Give You a complete</p>
    <div class="more">VIEW MORE &nbsp;›</div>
  </div>
  <div class="abs divider" style="left:199px"></div>

  <div class="service" style="left:200px">
    <svg width="74" height="74" viewBox="0 0 74 74"><circle cx="37" cy="37" r="33" fill="#fff" stroke="var(--ring)" stroke-width="6"/><path d="M8 21a33 33 0 0 1 50-10" fill="none" stroke="var(--brand-dark)" stroke-width="6"/><g fill="var(--green)"><ellipse cx="37" cy="29" rx="8" ry="3"/><path d="M29 31.5q8 4 16 0v3.5q-8 4-16 0z"/><path d="M29 37q8 4 16 0v3.5q-8 4-16 0z"/><path d="M29 42.5q8 4 16 0V46q-8 4-16 0z"/></g></svg>
    <h3>AUTOMATION</h3>
    <p>"But I must explain to you how all this And praising pain was born and I will Give You a complete</p>
    <div class="more">VIEW MORE &nbsp;›</div>
  </div>
  <div class="abs divider" style="left:354px"></div>

  <div class="service" style="left:355px">
    <svg width="74" height="74" viewBox="0 0 74 74"><circle cx="37" cy="37" r="33" fill="#fff" stroke="var(--ring)" stroke-width="6"/><path d="M10 56a33 33 0 0 1 0-38" fill="none" stroke="var(--brand-dark)" stroke-width="6"/><path d="M37 27a6 6 0 0 0-3.5 11v4h7v-4A6 6 0 0 0 37 27z" fill="none" stroke="var(--green)" stroke-width="1.8"/><rect x="34" y="44" width="6" height="2" fill="var(--green)"/></svg>
    <h3>PROJECT MANAGEMENT</h3>
    <p>"But I must explain to you how all this And praising pain was born and I will Give You a complete</p>
    <div class="more">VIEW MORE &nbsp;›</div>
  </div>
  <div class="abs divider" style="left:510px"></div>

  <div class="service" style="left:509px">
    <svg width="74" height="74" viewBox="0 0 74 74"><circle cx="37" cy="37" r="33" fill="#fff" stroke="var(--ring)" stroke-width="6"/><path d="M6 49a33 33 0 0 0 60 0" fill="none" stroke="var(--brand-dark)" stroke-width="6"/><g fill="none" stroke="var(--green)" stroke-width="2.6" stroke-dasharray="2 1.6"><circle cx="33" cy="39" r="5"/><circle cx="42" cy="31" r="3.5"/></g></svg>
    <h3>SERVICE STAFFING</h3>
    <p>"But I must explain to you how all this And praising pain was born and I will Give You a complete</p>
    <div class="more">VIEW MORE &nbsp;›</div>
  </div>
</section>

<h2 class="abs section-title col-title" style="left:58px;width:368px">TESTIMONIALS</h2>
<h2 class="abs section-title col-title" style="left:460px;width:190px">CUSTOMER LOG-IN</h2>

<section class="abs card testimonial">
  <div class="abs avatar" role="img" aria-label="Client portrait"></div>
  <div class="abs author">ALAN REYES</div>
  <span class="abs qmark" style="left:12px;top:80px">“</span>
  <p class="abs quote">Provident, similique sunt in culpa qui officia deserunt mollitia animi, id est laborum et dolorum fuga. Et harum quidem rerum facilis est et expedita Distinctio On the other hand, we denounce with righteous indignation and dislike men who are so beguiled and demoralized by the</p>
  <span class="abs qmark" style="left:317px;top:117px">”</span>
</section>

<section class="abs card login">
  <div class="field" style="top:17px">Name *</div>
  <div class="field" style="top:42px">Email *</div>
  <div class="field" style="top:67px;height:33px">Subject *</div>
  <a class="abs btn login-btn">LOGIN</a>
</section>

<footer class="abs footer">
  <h4 style="left:58px">ABOUT TALVERA</h4>
  <p class="abs footer-about">On the other hand, we denounce with righteous indignation and dislike men who are so beguiled and demoralized by the charms of pleasure of the moment, so blinded by desire, that they cannot foresee the pain and trouble that are bound to fectly simple and easy to distinguish....</p>
  <div class="abs footer-maker">DRESGAN</div>

  <h4 style="left:310px">FOOTER MENU</h4>
  <ul class="abs footer-menu">
    <li>Home</li><li>About us</li><li>Services</li><li>Customer Log-in</li><li>Testimonials</li><li>Contact</li>
  </ul>

  <h4 style="left:440px">LATEST NEWS</h4>
  <div class="abs news" style="top:46px">
    <div class="news-thumb" role="img" aria-label="News photo"></div>
    <p>Must explain to you how all this mistaken idea of denounc-ing pleasure and praising pain<br>JANUARY 14, 2015</p>
  </div>
  <div class="abs news" style="top:87px">
    <div class="news-thumb" role="img" aria-label="News photo"></div>
    <p>Must explain to you how all this mistaken idea of denounc-ing pleasure and praising pain<br>JANUARY 14, 2015</p>
  </div>
</footer>

<div class="abs copy-bar">
  <p class="abs copy">Copyrights@talvera.2015.Allrights reserved</p>
  <div class="abs social" aria-label="Social media links"><span></span><span></span><span></span><span></span><span></span><span></span></div>
</div>

</body>
</html>
```